Quillmoor 2006 Ltd
PaviMark Member
Quillmoor 2006 Ltd - Construction
Creative Brief
Simple
Rebecca Holloway
Administration
52 Kerrigan Street Ashworth 7712
becs@quillmoor.co.nz
www.quillmoor.co.nz
The PaviMark Logo needs to be on everything as well it dosent need to be big or main focus. I am in need of a Signature for my emails to,
All residential & commercial building products Decking, Fencing Rural & Domestic, Retainer Walls, Custom Made Trellis, Varnell Panels & Fencing, General Timber & Hardware, Macrocarpa Garden Sleepers, Through Post & rail (Kitset), Ply Wood The Best Quality for the Best Price

```html
<!DOCTYPE html>
<html lang="en">
<head>
<meta charset="utf-8">
<title>Quillmoor 2006 Ltd — Stationery Concepts</title>
<link href="https://fonts.googleapis.com/css2?family=Arimo:wght@400;700&family=Tinos&display=swap" rel="stylesheet">
<style>
:root{
  --bg-edge:#5a5a5a;
  --bg-mid:#9c9c9c;
  --ink:#1a1a1a;
  --paper:#ffffff;
  --yellow:#f4bd2a;
  --black:#111111;
  --muted:#6d6d6d;
  --label:#dcdcdc;
}
*{margin:0;padding:0;box-sizing:border-box}
html,body{width:1200px;height:497px;overflow:hidden}
body{
  position:relative;
  font-family:"Arimo",Arial,sans-serif;
  color:var(--ink);
  background:linear-gradient(180deg,var(--bg-edge) 0%,var(--bg-mid) 45%,var(--bg-mid) 60%,var(--bg-edge) 100%);
}
.abs{position:absolute}

/* Wordmark: invented name, one weight, one colour, one plain square */
.wordmark{display:flex;align-items:center;gap:0.25em;font-weight:400;letter-spacing:-0.02em;line-height:1;color:var(--black);white-space:nowrap}
.wordmark::after{content:"";width:0.32em;height:0.32em;background:var(--yellow);flex:none}

.title-block{left:20px;top:82px;width:200px}
.title-block .wordmark{font-size:34px}
.title-block .subtitle{font-family:"Tinos",serif;font-size:10px;color:#2a2a2a;margin:8px 0 0 48px}

.card{position:absolute;width:98px;height:100px;background:var(--paper);box-shadow:0 2px 5px rgba(0,0,0,.35);padding:9px 7px;font-size:4px;line-height:1.55}
.card .wordmark{font-size:15px}
.card .contact{margin-top:13px}
.card .contact li{list-style:none;display:flex;gap:3px;align-items:center}
.card .dot{width:4px;height:4px;border-radius:50%;background:var(--ink);flex:none}
.card .member{position:absolute;right:6px;bottom:30px;display:flex;align-items:center;gap:2px;font-size:4.5px}
.card .member i{width:5px;height:5px;background:var(--muted);display:block}
.services li{list-style:none;display:flex;gap:3px;align-items:flex-start;margin-bottom:2.6px}
.services li::before{content:"";width:3px;height:3px;margin-top:1.5px;background:currentColor;flex:none}
.card.back{padding-top:11px}
.card.yellow{background:var(--yellow)}
.card.black{background:var(--black);color:#eee}
.card.tall{height:106px;padding-top:12px}

.label{position:absolute;font-size:5px;color:var(--label);text-align:center}

.letterhead{left:434px;top:29px;width:330px;height:422px;background:var(--paper);box-shadow:0 3px 8px rgba(0,0,0,.35)}
.letterhead .fold{position:absolute;left:0;width:5px;height:13px;background:var(--black)}
.letterhead .wordmark{position:absolute;left:150px;top:40px;font-size:24px}
.letterhead .footer{position:absolute;left:0;right:0;bottom:16px;text-align:center;font-size:4px;color:var(--muted);line-height:1.7}

.env-back-brand{position:absolute;left:886px;top:197px;font-size:11px;font-weight:400;color:var(--black);transform:rotate(4deg)}
.env-front{position:absolute;left:772px;top:262px;width:404px;height:170px;background:var(--paper);box-shadow:0 3px 8px rgba(0,0,0,.35)}
.env-front .wordmark{position:absolute;left:22px;top:26px;font-size:24px}
.env-front .addr{position:absolute;left:22px;top:56px;font-size:4px;color:var(--muted)}
</style>
</head>
<body>

<header class="abs title-block">
  <div class="wordmark">Quillmoor</div>
  <p class="subtitle">Stationery Concepts</p>
</header>

<section class="card" style="left:19px;top:201px">
  <div class="wordmark">Quillmoor</div>
  <ul class="contact">
    <li><b>Rebecca Holloway</b></li>
    <li>Administration</li>
    <li><span class="dot"></span>52 Kerrigan Street</li>
    <li><span class="dot"></span>03 418 2265</li>
    <li><span class="dot"></span>becs@quillmoor.co.nz</li>
    <li><span class="dot"></span>www.quillmoor.co.nz</li>
  </ul>
  <div class="member"><i></i>PaviMark</div>
</section>
<p class="label" style="left:19px;top:306px;width:98px">Business Card</p>

<section class="card back" style="left:123px;top:201px">
  <ul class="services">
    <li>All residential &amp; commercial building products</li>
    <li>Decking, Fencing Rural &amp; Domestic</li>
    <li>Retainer Walls, Custom Made Trellis</li>
    <li>Varnell Panels &amp; Fencing</li>
    <li>General Timber &amp; Hardware</li>
    <li>Macrocarpa Garden Sleepers</li>
    <li>Through Post &amp; rail (Kitset), Ply Wood</li>
    <li>The Best Quality for the Best Price</li>
  </ul>
</section>
<p class="label" style="left:123px;top:306px;width:98px">Back Card Option 1</p>

<section class="card yellow tall" style="left:19px;top:343px">
  <ul class="services">
    <li>All residential &amp; commercial building products</li>
    <li>Decking, Fencing Rural &amp; Domestic</li>
    <li>Retainer Walls, Custom Made Trellis</li>
    <li>Varnell Panels &amp; Fencing</li>
    <li>General Timber &amp; Hardware</li>
    <li>Macrocarpa Garden Sleepers</li>
    <li>Through Post &amp; rail (Kitset), Ply Wood</li>
    <li>The Best Quality for the Best Price</li>
  </ul>
</section>
<p class="label" style="left:19px;top:456px;width:98px">Back Card Option 2</p>

<section class="card black tall" style="left:123px;top:343px">
  <ul class="services">
    <li>All residential &amp; commercial building products</li>
    <li>Decking, Fencing Rural &amp; Domestic</li>
    <li>Retainer Walls, Custom Made Trellis</li>
    <li>Varnell Panels &amp; Fencing</li>
    <li>General Timber &amp; Hardware</li>
    <li>Macrocarpa Garden Sleepers</li>
    <li>Through Post &amp; rail (Kitset), Ply Wood</li>
    <li>The Best Quality for the Best Price</li>
  </ul>
</section>
<p class="label" style="left:123px;top:456px;width:98px">Back Card Option 3</p>

<section class="abs letterhead">
  <span class="fold" style="top:14px"></span>
  <span class="fold" style="top:140px"></span>
  <div class="wordmark">Quillmoor</div>
  <div class="footer">
    52 Kerrigan Street, Ashworth 7712<br>
    P 03 418 2265 &nbsp; E becs@quillmoor.co.nz &nbsp; W www.quillmoor.co.nz
  </div>
</section>
<p class="label" style="left:434px;top:458px;width:330px">Letterhead</p>

<svg class="abs" style="left:0;top:0" width="1200" height="497" aria-hidden="true">
  <!-- back envelope, yellow flap -->
  <polygon points="786,52 1186,40 1190,150 790,170" fill="var(--paper)"/>
  <polygon points="786,52 1186,40 1188,96 990,120" fill="var(--yellow)"/>
  <!-- middle envelope, black flap -->
  <polygon points="780,130 1182,100 1190,230 790,250" fill="var(--paper)"/>
  <polygon points="780,130 1182,100 1190,130 1010,180 900,160" fill="var(--black)"/>
</svg>
<div class="env-back-brand">Quillmoor</div>

<section class="env-front">
  <div class="wordmark">Quillmoor</div>
  <p class="addr">52 Kerrigan Street, Ashworth 7712</p>
</section>
<p class="label" style="left:772px;top:456px;width:404px">Envelope</p>

</body>
</html>
```